QVM Business Card Design

We need a refreshed business card. Our company is a venture capital investment firm focused on investing in medical devices. Logo is attached. please also see our website www.qvmholdings.example

Target Market(s)

investors and potential investment targets

Industry/Entity Type

medical investments

Contact Information for Business Card

logo, name, title, email, phone, website, address,

Colors
0054AA
0677BA
7BADD7
CADEEF
E8F1F8
0094D4
00A9DD
6FCCEA
C7EBF8
E9F6FB
00AB8E
00BBA5
67D7C9
C6EFE9
E9F9F6

Requirements
Must have
• fresh modern design
Nice to have
• QR code leading to our linked in page, short description of what we do “Early Stage Medical Device Investors”

```html
<!DOCTYPE html>
<html lang="en">
<head>
<meta charset="utf-8">
<title>QVM Business Card</title>
<link href="https://fonts.googleapis.com/css2?family=Montserrat:wght@300;400;500;700;800&display=swap" rel="stylesheet">
<style>
  :root {
    --bg: #e4e6ea;
    --card: #ffffff;
    --blue: #0054aa;
    --teal: #00ab8e;
    --ink: #1d1d1f;
    --grey: #555a60;
    --mist-1: #e9f6fb;
    --mist-2: #a9c7e6;
    --mist-3: #8f95d3;
  }
  * { margin: 0; padding: 0; box-sizing: border-box; }
  html, body { width: 1200px; height: 900px; overflow: hidden; }
  body {
    background: var(--bg);
    font-family: "Montserrat", sans-serif;
    color: var(--ink);
    position: relative;
  }
  .card {
    position: absolute;
    width: 600px;
    height: 343px;
    overflow: hidden;
    box-shadow: 0 10px 28px rgba(0,0,0,.18);
    background: var(--card);
  }
  .card--front { left: 70px; top: 60px; }
  .card--back { left: 530px; top: 497px; }

  .front-visual {
    position: absolute; inset: 0;
    background:
      radial-gradient(ellipse at 58% 55%, #ffffff 0%, #e6f1f9 18%, rgba(169,199,230,.7) 45%, transparent 75%),
      linear-gradient(110deg, var(--mist-1) 0%, var(--mist-2) 50%, var(--mist-3) 100%);
  }

  .brand {
    position: absolute;
    display: flex;
    align-items: center;
  }
  .brand__name {
    font-weight: 800;
    color: var(--blue);
    letter-spacing: 1px;
    line-height: 1;
  }
  .brand__divider {
    width: 1px;
    background: var(--grey);
    align-self: stretch;
  }
  .brand__tagline {
    font-weight: 400;
    color: var(--grey);
    text-transform: uppercase;
    letter-spacing: 2.5px;
    line-height: 1.05;
  }

  .card--front .brand { left: 150px; top: 120px; height: 100px; }
  .card--front .brand__name { font-size: 78px; margin-right: 26px; }
  .card--front .brand__divider { margin-right: 22px; }
  .card--front .brand__tagline { font-size: 19px; }

  .card--back .brand { left: 40px; top: 120px; height: 76px; }
  .card--back .brand__name { font-size: 58px; margin-right: 20px; }
  .card--back .brand__divider { margin-right: 16px; }
  .card--back .brand__tagline { font-size: 13px; letter-spacing: 2px; }

  .contact-divider {
    position: absolute; left: 330px; top: 80px;
    width: 1.5px; height: 150px; background: var(--teal);
  }
  .contact {
    position: absolute; left: 350px; top: 62px;
  }
  .contact__name {
    font-weight: 800; font-size: 22px; letter-spacing: .3px;
    text-transform: uppercase;
  }
  .contact__first { color: var(--blue); }
  .contact__last { color: var(--teal); }
  .contact__title { font-size: 14px; font-weight: 500; margin-top: 2px; }
  .contact__address { font-size: 14px; font-weight: 500; margin-top: 16px; line-height: 1.35; }
  .contact__list { list-style: none; margin-top: 14px; font-size: 14px; font-weight: 500; }
  .contact__list li { display: flex; align-items: center; gap: 8px; line-height: 1.45; }
  .contact__icon { width: 14px; height: 14px; flex: none; }

  .footer-bands { position: absolute; left: 0; bottom: 0; width: 600px; height: 80px; }
  .website {
    position: absolute; right: 16px; bottom: 18px;
    color: #fff; font-size: 16px; font-weight: 500; letter-spacing: .3px;
    line-height: 1;
  }
</style>
</head>
<body>

<section class="card card--front" aria-label="Card front">
  <div class="front-visual" role="img" aria-label="Soft-focus close-up photograph of a blue medical stent mesh"></div>
  <div class="brand">
    <span class="brand__name">QVM</span>
    <span class="brand__divider"></span>
    <span class="brand__tagline">Quantum<br>Vital<br>Medtech</span>
  </div>
</section>

<section class="card card--back" aria-label="Card back">
  <div class="brand">
    <span class="brand__name">QVM</span>
    <span class="brand__divider"></span>
    <span class="brand__tagline">Quantum<br>Vital<br>Medtech</span>
  </div>

  <div class="contact-divider"></div>

  <div class="contact">
    <h1 class="contact__name"><span class="contact__first">Dana</span> <span class="contact__last">Whitford</span></h1>
    <p class="contact__title">Managing Director</p>
    <p class="contact__address">Harbor Point 1200 Park<br>Avenue North Suite 310</p>
    <ul class="contact__list">
      <li>
        <svg class="contact__icon" viewBox="0 0 24 24" aria-hidden="true"><path fill="#00ab8e" d="M6.6 10.8a15.1 15.1 0 0 0 6.6 6.6l2.2-2.2c.3-.3.7-.4 1-.2 1.1.4 2.3.6 3.6.6.6 0 1 .4 1 1V20c0 .6-.4 1-1 1A17 17 0 0 1 3 4c0-.6.4-1 1-1h3.5c.6 0 1 .4 1 1 0 1.3.2 2.5.6 3.6.1.3 0 .7-.2 1z"/></svg>
        +61 400 000 123
      </li>
      <li>
        <svg class="contact__icon" viewBox="0 0 24 24" aria-hidden="true"><path fill="#00ab8e" d="M2 5h20v14H2z"/><path d="M2 5l10 8 10-8" fill="none" stroke="#fff" stroke-width="1.8"/></svg>
        info@qvmholdings.example
      </li>
    </ul>
  </div>

  <svg class="footer-bands" viewBox="0 0 600 80" aria-hidden="true">
    <polygon points="0,68 310,54 300,80 0,80" fill="#0054aa"/>
    <polygon points="330,30 600,14 600,80 316,80" fill="#00ab8e"/>
  </svg>
  <span class="website">www.qvmholdings.example</span>
</section>

</body>
</html>
```